Vantrel Web Services

This is a new It services company operating in Perth western Australia

we need a website that is easy to navigate without a cluttered feel to it it should have the following links and pages

About Us
Services
Clients
Contact Us
MY Vantrel (login for clients)

Hi it is a web based IT services company so we would expect customers to come to the website for 2 different purposes the first is to enquire about our services and then as they become customers come to our website to manage their services so whilst they are seperate we want do not want it to look like 2 different websites

hope this helps

Hi to update this we need a home page and templates for sub pages

this is a design brief only and not the coding of the pages or building of the site

```html
<!DOCTYPE html>
<html lang="en">
<head>
<meta charset="utf-8">
<title>Vantrel Web Services</title>
<link rel="stylesheet" href="https://fonts.googleapis.com/css2?family=Roboto:wght@300;400;700&family=Michroma&family=Arimo:wght@400;700&display=swap">
<style>
:root{
  --red:#b5120f;
  --red-dark:#8e0b09;
  --blue:#04299a;
  --blue-link:#1b5bd6;
  --title-blue:#0a2d9c;
  --ink:#2b2b2b;
  --grey:#666;
  --footer-bg:#111;
}
*{margin:0;padding:0;box-sizing:border-box}
html,body{width:1023px;height:1200px;overflow:hidden;background:#fff}
body{font-family:"Arimo",Arial,sans-serif;color:var(--ink);position:relative}
a{text-decoration:none;color:inherit}

.site-header{position:absolute;left:0;top:0;width:1023px;height:66px;background:linear-gradient(#fdfdfd,#d9d9d9)}
.brand-name{position:absolute;font-family:"Arimo",Arial,sans-serif;font-weight:700}
.site-header .brand-name{left:120px;top:16px;font-size:28px;line-height:34px;color:var(--red)}
.utility-links{position:absolute;right:117px;top:43px;font-size:9.5px;color:#333}
.utility-links span{margin:0 4px}

.main-nav{position:absolute;left:0;top:66px;width:1023px;height:42px;background:linear-gradient(#2a2a2a,#141414);border-top:1px solid #000;border-bottom:1px solid #000}
.main-nav ul{list-style:none;position:absolute;left:120px;top:9px;display:flex;gap:6px}
.main-nav a{display:block;width:126px;height:23px;line-height:23px;text-align:center;border-radius:8px;
  background:linear-gradient(#d8221c,var(--red-dark));color:#fff;font-family:"Michroma",sans-serif;font-size:9.5px;text-transform:uppercase}
.main-nav a.is-active{background:linear-gradient(#3f63c8,#1a3a98)}

.hero{position:absolute;left:0;top:108px;width:1023px;height:346px;
  background:linear-gradient(100deg,#9db3d8 0%,#3d5fa8 30%,#0f2a6e 55%,#2c4f9c 75%,#1a1f38 100%)}

.pillars{position:absolute;left:0;top:454px;width:1023px;height:228px;background:var(--blue);border-top:2px solid #04164f}
.pillar{position:absolute;top:-28px;width:260px;text-align:center;color:#fff}
.pillar-icon{width:102px;height:102px;margin:0 auto;border-radius:50%;background:radial-gradient(circle at 50% 35%,#fff,#d7d7d7);border:2px solid #0b1a44;display:flex;align-items:center;justify-content:center}
.pillar h2{font-family:"Roboto",sans-serif;font-weight:300;font-size:31px;margin-top:22px;line-height:36px}
.pillar p{font-size:12px;line-height:14.5px;margin-top:6px}

.why{position:absolute;left:116px;top:722px;width:480px}
.section-title{font-family:"Roboto",sans-serif;font-weight:300;font-size:31px;color:#1a1a1a;line-height:36px}
.why .lead{font-size:12px;line-height:14.5px;margin-top:5px;color:#333}
.why-photo{position:absolute;left:2px;top:84px;width:155px;height:128px;border:2px solid #ccc;background:linear-gradient(135deg,#cfdbe6,#7d97b4 60%,#3b4a5e)}
.why-text{position:absolute;left:171px;top:94px;width:303px;font-size:12px;line-height:14.5px;color:#333}
.read-more{display:block;margin-top:8px;color:var(--red)}

.news{position:absolute;left:661px;top:722px;width:260px}
.news-list{margin-top:14px}
.news-item{position:relative;height:103px}
.news-item::after{content:"";position:absolute;left:2px;right:0;top:77px;border-bottom:1px dotted #555}
.news-date{position:absolute;left:0;top:0;width:27px;text-align:center}
.news-day{display:block;width:27px;height:27px;border-radius:50%;background:var(--red-dark);color:#fff;font-family:"Roboto",sans-serif;font-weight:700;font-size:15px;line-height:27px}
.news-month{display:block;font-size:10px;font-weight:700;color:var(--red-dark);margin-top:4px}
.news-body{position:absolute;left:47px;top:0;width:212px}
.news-body h3{font-size:11px;line-height:14.5px;color:var(--title-blue);width:205px}
.news-body p{font-size:9.5px;line-height:12px;color:var(--grey);margin-top:2px;width:200px}

.site-footer{position:absolute;left:0;top:1034px;width:1023px;height:166px;background:var(--footer-bg)}
.site-footer .brand-name{left:99px;top:28px;font-size:20px;line-height:30px;color:#fff}
.footer-col{position:absolute;top:26px}
.footer-col h4{font-family:"Roboto",sans-serif;font-weight:400;font-size:14.5px;color:#fff}
.footer-col ul{list-style:none;margin-top:10px}
.footer-col li{font-size:10.5px;line-height:18.8px;color:var(--blue-link);padding-left:10px;position:relative}
.footer-col li::before{content:"";position:absolute;left:0;top:7px;border-left:3px solid #fff;border-top:2.5px solid transparent;border-bottom:2.5px solid transparent}
.newsletter-input{position:absolute;left:0;top:29px;width:158px;height:21px;background:#1d1d1d;border:1px solid #3a3a3a;border-radius:3px;color:#aaa;font-size:10px;line-height:19px;padding-left:13px}
.subscribe{position:absolute;left:93px;top:59px;width:69px;height:22px;border-radius:4px;background:linear-gradient(#2f8cf0,#1463cc);color:#fff;font-size:10.5px;line-height:22px;text-align:center}
</style>
</head>
<body>

<header class="site-header">
  <span class="brand-name">Vantrel</span>
  <nav class="utility-links"><a>Support</a><span>|</span><a>FAQs</a><span>|</span><a>Testimonials</a><span>|</span><a>Help</a></nav>
</header>

<nav class="main-nav">
  <ul>
    <li><a class="is-active">Home</a></li>
    <li><a>About Us</a></li>
    <li><a>Services</a></li>
    <li><a>Clients</a></li>
    <li><a>Contact Us</a></li>
    <li><a>My Vantrel</a></li>
  </ul>
</nav>

<div class="hero" role="img" aria-label="Blue-toned photo of an office tower and a businessman holding a laptop"></div>

<section class="pillars">
  <div class="pillar" style="left:99px">
    <div class="pillar-icon">
      <svg width="52" height="58" viewBox="0 0 52 58"><path d="M26 3 L47 10 V28 C47 42 37 51 26 55 C15 51 5 42 5 28 V10 Z" fill="none" stroke="#0a2d9c" stroke-width="4"/><path d="M26 11 L40 16 V29 C40 39 33 45 26 48 Z" fill="#0a2d9c"/></svg>
    </div>
    <h2>ADVANTAGES</h2>
    <p>Lorem ipsum dolor sit amet, consectetur adipisicing elit, sed do eiusmod tempor incididunt ut labore et dolore magna aliqua.</p>
  </div>
  <div class="pillar" style="left:371px">
    <div class="pillar-icon">
      <svg width="56" height="56" viewBox="0 0 56 56"><circle cx="28" cy="28" r="25" fill="#0a2d9c"/><circle cx="28" cy="28" r="16" fill="#fff"/><rect x="19" y="29" width="5" height="9" fill="#0a2d9c"/><rect x="26" y="24" width="5" height="14" fill="#0a2d9c"/><rect x="33" y="19" width="5" height="19" fill="#0a2d9c"/><path d="M28 3 V12" stroke="#fff" stroke-width="3"/></svg>
    </div>
    <h2>MISSION</h2>
    <p>Sed ut perspiciatis, unde omnis iste natus error sit voluptatem accusantium doloremque laudantium, totam rem aperiam.</p>
  </div>
  <div class="pillar" style="left:649px">
    <div class="pillar-icon">
      <svg width="64" height="64" viewBox="0 0 64 64" fill="#0a2d9c"><circle cx="32" cy="32" r="14"/><path d="M32 2 L38 10 H26Z M32 62 L26 54 H38Z M2 32 L10 26 V38Z M62 32 L54 38 V26Z M11 11 L20 13 L13 20Z M53 53 L44 51 L51 44Z M53 11 L51 20 L44 13Z M11 53 L13 44 L20 51Z"/></svg>
    </div>
    <h2>VISION</h2>
    <p>Lorem ipsum dolor sit amet, consectetur adipisicing elit, sed do eiusmod tempor incididunt ut labore et dolore magna aliqua.</p>
  </div>
</section>

<section class="why">
  <h2 class="section-title">WHY CHOOSE VANTREL?</h2>
  <p class="lead">At vero eos et accusamus et iusto odio dignissimos ducimus, qui blanditiis praesentium voluptatum deleniti atque corrupti, quos dolores et quas molestias excepturi sint.</p>
  <div class="why-photo" role="img" aria-label="Photo of hands typing on a laptop keyboard"></div>
  <div class="why-text">
    <p>Obcaecati cupiditate non provident, similique sunt in culpa, qui officia deserunt mollitia animi, id est laborum et dolorum fuga.At vero eos et accusamus et iusto odio dignissimos ducimus, qui blanditiis praesentium voluptatum deleniti atque corrupti, quos dolores et quas molestias excepturi sint.</p>
    <a class="read-more">read more +</a>
  </div>
</section>

<section class="news">
  <h2 class="section-title">LATEST NEWS</h2>
  <div class="news-list">
    <article class="news-item">
      <div class="news-date"><span class="news-day">27</span><span class="news-month">Mar</span></div>
      <div class="news-body">
        <h3>We develop our own sofrtware APPS and offer business and IT services</h3>
        <p>Lorem ipsum dolor sit amet, consectetur adipisicing elit, sed do eiusmod tempor incididunt ut labore et dolore magna aliqua.</p>
      </div>
    </article>
    <article class="news-item">
      <div class="news-date"><span class="news-day">12</span><span class="news-month">Feb</span></div>
      <div class="news-body">
        <h3>We develop our own sofrtware APPS and offer business and IT services</h3>
        <p>Lorem ipsum dolor sit amet, consectetur adipisicing elit, sed do eiusmod tempor incididunt ut labore et dolore magna aliqua.</p>
      </div>
    </article>
  </div>
</section>

<footer class="site-footer">
  <span class="brand-name">Vantrel</span>
  <div class="footer-col" style="left:289px">
    <h4>Why Us</h4>
    <ul><li>Our Clients</li><li>Technology</li><li>Soft Labs</li></ul>
  </div>
  <div class="footer-col" style="left:391px">
    <h4>Quick Links</h4>
    <ul><li>Lorem ipsum dolor</li><li>Amet consectetuer</li><li>Mauris vel tortor vitae</li><li>Nibh condimentum</li></ul>
  </div>
  <div class="footer-col" style="left:562px">
    <h4>Support</h4>
    <ul><li>Nibh condimentum</li><li>Integer ac lacus</li><li>Sociis natoque</li><li>Enatibus et magnis</li></ul>
  </div>
  <div class="footer-col" style="left:732px">
    <h4>Newsletter:</h4>
    <div class="newsletter-input">Enter your email here</div>
    <div class="subscribe">SUBSCRIBE</div>
  </div>
</footer>

</body>
</html>
```